Retractable Banner Design Featuring Key Product for Beauty Trade Show

We're a beauty/nail supply company that specializes in products used in professional nail salons. The key product for this design is Disposable Latex Gloves.
We will be exhibiting in a trade show this summer and are looking for a free-standing Retractable Banner Design that will be displayed at the front of our booth. The goal of the banner will be to display key products that are high in demand with our customers. The banner will be used to attract attention and highlight key selling points of these popular products. We would like the banner to be focused on the product title, image and key points, with a beauty/model/pattern background to create a professional appearance.
Nail Salons
Nail & Beauty Industry

```html
<!DOCTYPE html>
<html lang="en">
<head>
<meta charset="UTF-8">
<title>Latex Gloves Retractable Banner</title>
<link href="https://fonts.googleapis.com/css2?family=Poppins:wght@600;700;800&display=swap" rel="stylesheet">
<style>
  :root {
    --page-bg: #ededed;
    --banner-gray: #e9e9e9;
    --orange-top: #c45a22;
    --orange-mid: #e57a2f;
    --orange-deep: #a84a18;
    --white: #ffffff;
    --ink: #2a2a2a;
    --card: #f4f4f4;
  }
  * { margin: 0; padding: 0; box-sizing: border-box; }
  html, body { width: 1200px; height: 1173px; overflow: hidden; }
  body {
    background: var(--page-bg);
    font-family: "Poppins", sans-serif;
    position: relative;
  }
  .banner {
    position: absolute;
    left: 378px;
    top: 20px;
    width: 445px;
    height: 1133px;
    background: var(--banner-gray);
    overflow: hidden;
    box-shadow: 0 6px 24px rgba(0,0,0,0.12);
  }
  .banner__photo {
    position: absolute;
    left: 0; top: 0;
    width: 100%; height: 366px;
    background: linear-gradient(160deg, #f3f3f3 0%, #dcdcdc 55%, #e8d6cb 100%);
  }
  .banner__orange {
    position: absolute;
    left: 0; top: 366px;
    width: 100%; height: 767px;
    background: linear-gradient(180deg, var(--orange-top) 0%, var(--orange-mid) 45%, var(--orange-mid) 60%, var(--orange-deep) 100%);
  }
  .banner__product {
    position: absolute;
    left: 40px; top: 150px;
    width: 385px; height: 274px;
    background: linear-gradient(135deg, #f7f7f7 0%, #f2f2f2 45%, #e7692a 100%);
    border-radius: 2px;
  }
  .title {
    position: absolute;
    left: 0; width: 100%;
    text-align: center;
    color: var(--white);
    font-weight: 800;
    line-height: 1;
    text-shadow: 0 3px 4px rgba(0,0,0,0.25);
  }
  .title--latex { top: 432px; font-size: 112px; letter-spacing: -1px; }
  .title--gloves { top: 530px; font-size: 96px; letter-spacing: -1px; }
  .stats {
    position: absolute;
    left: 52px; top: 641px;
    width: 348px; height: 102px;
    background: var(--card);
    border-radius: 18px;
    display: flex;
    align-items: center;
    color: var(--ink);
  }
  .stats__item {
    flex: 1;
    text-align: center;
    line-height: 1;
  }
  .stats__item + .stats__item { border-left: 2px solid var(--ink); }
  .stats__number { font-size: 50px; font-weight: 700; display: block; }
  .stats__label { font-size: 17px; font-weight: 600; display: block; margin-top: 2px; }
  .points__heading {
    position: absolute;
    left: 58px; top: 752px;
    color: var(--white);
    font-size: 23px;
    font-weight: 700;
    padding-bottom: 4px;
    border-bottom: 2px solid var(--white);
    width: 175px;
  }
  .points {
    position: absolute;
    left: 52px; top: 808px;
    list-style: none;
  }
  .points__item {
    display: flex;
    align-items: flex-start;
    height: 62px;
    color: var(--white);
  }
  .points__tick { width: 42px; height: 42px; flex: none; margin-top: 2px; }
  .points__text {
    margin-left: 14px;
    font-size: 19px;
    font-weight: 700;
    line-height: 1.25;
    text-transform: uppercase;
  }
</style>
</head>
<body>
  <div class="banner">
    <div class="banner__photo" role="img" aria-label="Photo of hands pulling on a white latex glove on a light grey background"></div>
    <div class="banner__orange"></div>
    <div class="banner__product" role="img" aria-label="Photo of orange and white boxes of textured latex gloves, size small"></div>

    <div class="title title--latex">LATEX</div>
    <div class="title title--gloves">GLOVES</div>

    <div class="stats">
      <div class="stats__item">
        <span class="stats__number">1,000</span>
        <span class="stats__label">Pcs/Case</span>
      </div>
      <div class="stats__item">
        <span class="stats__number">84</span>
        <span class="stats__label">Cases Per Pallet</span>
      </div>
    </div>

    <div class="points__heading">KEY POINTS:</div>
    <ul class="points">
      <li class="points__item">
        <svg class="points__tick" viewBox="0 0 42 42"><circle cx="20" cy="22" r="17" fill="none" stroke="#fff" stroke-width="3.5"/><path d="M11 22 L19 30 L38 6" fill="none" stroke="#fff" stroke-width="5" stroke-linecap="round" stroke-linejoin="round"/></svg>
        <span class="points__text">100% Powder-Free<br>No Residue or Irritants</span>
      </li>
      <li class="points__item">
        <svg class="points__tick" viewBox="0 0 42 42"><circle cx="20" cy="22" r="17" fill="none" stroke="#fff" stroke-width="3.5"/><path d="M11 22 L19 30 L38 6" fill="none" stroke="#fff" stroke-width="5" stroke-linecap="round" stroke-linejoin="round"/></svg>
        <span class="points__text">Premium Textured Grip<br>For Superior Grip</span>
      </li>
      <li class="points__item">
        <svg class="points__tick" viewBox="0 0 42 42"><circle cx="20" cy="22" r="17" fill="none" stroke="#fff" stroke-width="3.5"/><path d="M11 22 L19 30 L38 6" fill="none" stroke="#fff" stroke-width="5" stroke-linecap="round" stroke-linejoin="round"/></svg>
        <span class="points__text">6.2G Latex –<br>Super Heavy Duty</span>
      </li>
      <li class="points__item">
        <svg class="points__tick" viewBox="0 0 42 42"><circle cx="20" cy="22" r="17" fill="none" stroke="#fff" stroke-width="3.5"/><path d="M11 22 L19 30 L38 6" fill="none" stroke="#fff" stroke-width="5" stroke-linecap="round" stroke-linejoin="round"/></svg>
        <span class="points__text">Designed For<br>Professional Salons!</span>
      </li>
    </ul>
  </div>
</body>
</html>
```